Insulation Franchise Seasonal Content Creation

I am looking to launch some seasonal content and I would like 8 different designs that will go out as digital ads, Facebook and Instagram posts. The look and feel of the design: - Clean and neat - Simple Text, lots of open space (don’t want it to look too crowded) - Using branded colors that give a winter feel (brand guide to be provided) - Two separate texts areas in the design 1.) A sentence that identifies the pain point and explains the picture 2.) A sentence that is the call to action. See the attached ads for a general idea of the look we would like but I would like this design to stand out from those. I will provide copy, photos, branded colors, fonts and logos. Here is the copy I would like to use:
“Feeling the winter this year?” (pic of cold coming inside) “Let Wombit help keep the cold outside”
“Feel the winter creeping in?” “Air sealing and proper Insulation can eliminate those cool winter breezes in your home.”

“High heating bills? Why are you paying to melt the snow and ice on your roof?”
“Get your home well insulated with Wombit and keep your heat INSIDE where it should be” (Patchy snow on roofs)
“Storm damage to your home?” “Wombit can help by replacing wet and ruined insulation” (Before and after pics of damage)

Holiday Pain Points - Saving money / Visitors comfortability
“Snow on the roof means a well insulated home. Leave the snow for Santa to land on this year.” “Click here to learn how to keep your home comfortable and lower heating bills this winter” (pic of santa’s boots on the roof)
“Family complaining about the temperature in your house? Make sure your guests stay comfortable this holiday season” (pic of someone cold inside)
“Staying home this holiday season? Be comfortable and ensure your home is well-insulated.” “Contact Wombit for a free estimate”
Keep your money to spend on your holidays, not on your heating bill! Let Wombit help you save by correctly insulating your home!”

Target Market(s)

Homeowners, those interested in savings in their heating/cooling costs, energy efficiency

Industry/Entity Type

Home Improvement

Font styles to use
Sans Serif
Other font styles liked:
• Honey Lips, Bolt Rounded

Colors
0054AA
0677BA
7BADD7
CADEEF
E8F1F8
0094D4
00A9DD
6FCCEA
C7EBF8
E9F6FB
00AB8E
00BBA5
67D7C9
C6EFE9
E9F9F6

Requirements
Must have
• 2 separate text areas, photo and the logo
Should not have
• No pictures of the mascot, Tarro (the Wombit bear)

```html
<!DOCTYPE html>
<html lang="en">
<head>
<meta charset="UTF-8">
<title>Wombit Insulation – Feeling the winter this year?</title>
<link href="https://fonts.googleapis.com/css2?family=Poppins:wght@400;700&display=swap" rel="stylesheet">
<style>
  :root {
    --navy: #0054AA;
    --ocean: #0677BA;
    --sky: #7BADD7;
    --frost: #CADEEF;
    --ice: #E8F1F8;
    --azure: #0094D4;
    --cyan: #00A9DD;
    --teal: #00AB8E;
    --teal-light: #67D7C9;
    --panel-top: rgba(0, 84, 170, 0.78);
    --panel-bottom: rgba(0, 148, 212, 0.82);
    --white: #ffffff;
  }
  html, body {
    margin: 0;
    padding: 0;
    width: 1200px;
    height: 1200px;
    overflow: hidden;
  }
  .ad {
    position: relative;
    width: 1200px;
    height: 1200px;
    overflow: hidden;
    font-family: "Poppins", sans-serif;
    color: var(--white);
  }
  .ad__photo {
    position: absolute;
    inset: 0;
    background:
      radial-gradient(ellipse 420px 300px at 330px 420px, rgba(232, 241, 248, 0.75), transparent 70%),
      radial-gradient(ellipse 520px 420px at 850px 760px, rgba(123, 173, 215, 0.6), transparent 70%),
      radial-gradient(ellipse 380px 260px at 260px 900px, rgba(202, 222, 239, 0.55), transparent 70%),
      linear-gradient(160deg, var(--sky) 0%, var(--ocean) 55%, var(--navy) 100%);
  }
  .ad__panels {
    position: absolute;
    inset: 0;
  }
  .brand {
    position: absolute;
    top: 78px;
    left: 80px;
    display: flex;
    align-items: center;
    gap: 14px;
    font-weight: 700;
    font-size: 40px;
    color: var(--white);
    letter-spacing: 0.5px;
  }
  .brand__dot {
    width: 22px;
    height: 22px;
    border-radius: 50%;
    background: var(--teal);
  }
  .message {
    position: absolute;
    right: 62px;
    top: 770px;
    text-align: right;
  }
  .message__headline {
    margin: 0;
    font-weight: 700;
    font-size: 68px;
    line-height: 1.05;
  }
  .message__cta {
    margin: 26px 0 0;
    font-weight: 400;
    font-size: 30px;
    line-height: 1.35;
    color: var(--ice);
  }
</style>
</head>
<body>
  <main class="ad">
    <div class="ad__photo" role="img" aria-label="Photo of cold winter air and frost creeping in through a window into a home"></div>

    <svg class="ad__panels" width="1200" height="1200" viewBox="0 0 1200 1200" aria-hidden="true">
      <polygon points="668,0 1200,0 1200,536" fill="var(--panel-top)"/>
      <polygon points="384,1200 1200,280 1200,1200" fill="var(--panel-bottom)"/>
    </svg>

    <div class="brand">
      <span class="brand__dot"></span>
      <span class="brand__name">Wombit Insulation</span>
    </div>

    <section class="message">
      <h1 class="message__headline">Feeling<br>the winter<br>this year?</h1>
      <p class="message__cta">Let Wombit help keep<br>the cold outside</p>
    </section>
  </main>
</body>
</html>
```